Want a package created for a new protein bar

We would like a new package created for a new protein bar project The name of the bar will be VOLMBite a real food protein bar, we would like a ‘window’ on the package of bar like Brave Meadow bar below in images.

VOLMBite
‘Super Food Bar’
14g of Whey Protein
The package film size is the following 12cm width x 15cm Length,
Flavor Peanut Chocolate Chip, additional information will be attached shortly like nutrition facts,

Target Market(s)

fitness market, bodybuilders, athletes, everyday people

Industry/Entity Type

Health Product

Logo Text

VOLMBite

Font styles to use
Serif
Sans Serif
Decorative

Requirements
Must have
• Package window

```html
<!DOCTYPE html>
<html lang="en">
<head>
<meta charset="utf-8">
<title>VOLMBite Super Food Bar – Wrapper</title>
<link href="https://fonts.googleapis.com/css2?family=Baloo+2:wght@800&display=swap" rel="stylesheet">
<style>
  :root {
    --stage: #2a2a2a;
    --wrap-black: #121212;
    --wrap-edge: #1e1e1e;
    --orange-light: #f08a1c;
    --orange-mid: #e0661a;
    --orange-deep: #d8461a;
    --white: #ffffff;
    --ink: #111111;
    --nut-light: #e3b06a;
    --nut-dark: #6b3a1c;
  }
  html, body {
    margin: 0;
    padding: 0;
    width: 1200px;
    height: 964px;
    overflow: hidden;
    background: var(--stage);
  }
  .canvas {
    position: relative;
    width: 1200px;
    height: 964px;
  }
  .wrapper {
    position: absolute;
    left: 100px;
    top: 300px;
    width: 1000px;
    height: 360px;
  }
  .wrapper-crimps {
    position: absolute;
    inset: 0;
  }
  .brand-panel {
    position: absolute;
    left: 50px;
    top: 24px;
    width: 130px;
    height: 312px;
    background: var(--wrap-black);
  }
  .brand-name {
    position: absolute;
    left: 50%;
    top: 50%;
    transform: translate(-50%, -50%) rotate(-90deg);
    font-family: "Baloo 2", sans-serif;
    font-weight: 800;
    font-size: 64px;
    line-height: 1;
    color: var(--white);
    white-space: nowrap;
    letter-spacing: 1px;
  }
  .window {
    position: absolute;
    left: 180px;
    top: 24px;
    width: 170px;
    height: 312px;
    background: var(--wrap-black);
  }
  .window-view {
    position: absolute;
    left: 6px;
    top: 18px;
    right: 4px;
    bottom: 22px;
    background: linear-gradient(135deg, #d99a4c 0%, #b86a2a 40%, #5a2e16 60%, #e0a85c 100%);
  }
  .front-panel {
    position: absolute;
    left: 350px;
    top: 24px;
    width: 600px;
    height: 312px;
    background: linear-gradient(100deg, var(--orange-light) 0%, var(--orange-mid) 60%, var(--orange-deep) 100%);
  }
  .headline-band {
    position: absolute;
    left: 20px;
    top: 40px;
    width: 390px;
    height: 160px;
  }
  .headline {
    position: absolute;
    left: 60px;
    top: 52px;
    margin: 0;
    font-family: "Baloo 2", sans-serif;
    font-weight: 800;
    color: var(--white);
    line-height: 0.82;
    transform: rotate(-6deg);
    transform-origin: left top;
  }
  .headline .line-1 { display: block; font-size: 78px; }
  .headline .line-2 { display: block; font-size: 60px; padding-left: 10px; }
  .flavor-tag {
    position: absolute;
    left: 30px;
    top: 222px;
    padding: 6px 60px 4px 12px;
    background: var(--white);
    border-radius: 4px;
    font-family: "Baloo 2", sans-serif;
    font-weight: 800;
    font-size: 20px;
    line-height: 1.05;
    color: var(--ink);
    font-style: normal;
  }
  .ingredient-art {
    position: absolute;
    left: 250px;
    top: 170px;
    width: 260px;
    height: 130px;
    border-radius: 60px 70px 50px 40px;
    background: radial-gradient(ellipse at 55% 50%, var(--nut-light) 0%, #c98f4e 55%, rgba(107,58,28,0.0) 80%);
  }
  .protein-badge {
    position: absolute;
    left: 448px;
    top: 34px;
    width: 116px;
    height: 116px;
    border-radius: 50%;
    background: var(--white);
    font-family: "Baloo 2", sans-serif;
    font-weight: 800;
    color: var(--ink);
    text-align: center;
  }
  .protein-amount {
    display: block;
    margin-top: 10px;
    font-size: 58px;
    line-height: 0.9;
  }
  .protein-amount small { font-size: 40px; }
  .protein-label {
    display: block;
    font-size: 13px;
    line-height: 1.05;
  }
</style>
</head>
<body>
<div class="canvas">
  <div class="wrapper">
    <svg class="wrapper-crimps" width="1000" height="360" viewBox="0 0 1000 360" aria-hidden="true">
      <polygon fill="var(--wrap-black)" points="10,0 60,6 60,354 10,360 18,340 2,320 18,300 2,280 18,260 2,240 18,220 2,200 18,180 2,160 18,140 2,120 18,100 2,80 18,60 2,40 18,20"/>
      <polygon fill="var(--wrap-black)" points="940,6 990,0 982,20 998,40 982,60 998,80 982,100 998,120 982,140 998,160 982,180 998,200 982,220 998,240 982,260 998,280 982,300 998,320 982,340 990,360 940,354"/>
      <rect x="50" y="24" width="900" height="312" fill="var(--wrap-edge)"/>
    </svg>

    <div class="brand-panel">
      <span class="brand-name">VOLMBite</span>
    </div>

    <div class="window">
      <div class="window-view" role="img" aria-label="Window showing the bar inside: peanuts and almonds with chocolate drizzle"></div>
    </div>

    <div class="front-panel">
      <svg class="headline-band" viewBox="0 0 390 160" aria-hidden="true">
        <path fill="var(--ink)" d="M8,70 C30,40 120,30 220,18 C290,10 350,4 388,0 L360,40 L390,44 L350,80 L380,86 C300,110 200,140 60,158 C30,160 14,140 10,120 Z"/>
      </svg>
      <h1 class="headline"><span class="line-1">SUPER</span><span class="line-2">FOOD BAR</span></h1>

      <p class="flavor-tag">FLAVOR PEANUT<br>CHOCOLATE CHIP</p>

      <div class="ingredient-art" role="img" aria-label="Peanuts in shells with a chocolate curl and green leaves"></div>

      <div class="protein-badge">
        <span class="protein-amount">14<small>g</small></span>
        <span class="protein-label">OF WHEY<br>PROTEIN</span>
      </div>
    </div>
  </div>
</div>
</body>
</html>
```